real esate business card with company logo and name

we need a business card design for a real esate company

The company name is Walsh & Ortiz Pty Ltd, and we have our logo designed and will upload. We want classic or moden feel. Black or white background. looks more textured. Should include folowinginformations
Paul Walsh and Tara Ortiz
Sales Agents & Onsite Manager
p: 07 5948 2610
F: 07 5948 2795
M:0451 786 923
3/22 Marlow Crescent, ELLEN GROVE QLD 4078

We want this business card looks professonal. Thank you in advance.

Industry/Entity Type

Real Estate Agent

Contact Information for Business Card

Paul Walsh and Tara Ortiz
Onsite Manager & Sales Agents
p: 07 5948 2610
M:0451 786 923

Font styles to use
Serif

Colors
000000
fbfbfb
333333
959595

Requirements
Must have
• company logo and name, black or white back ground

```html
<!DOCTYPE html>
<html lang="en">
<head>
<meta charset="utf-8">
<title>Walsh &amp; Ortiz Pty Ltd — Business Card</title>
<link rel="stylesheet" href="https://fonts.googleapis.com/css2?family=Open+Sans:wght@400;600;700&display=swap">
<style>
  :root {
    --card-black: #000000;
    --card-deep: #0b0b0b;
    --ink-white: #fbfbfb;
    --ink-grey: #959595;
    --ink-dark: #333333;
    --silver-light: #e4e4e4;
    --silver-mid: #a8a8a8;
    --silver-dark: #6e6e6e;
    --backdrop: #e9e7e3;
  }
  * { box-sizing: border-box; margin: 0; padding: 0; }
  html, body {
    width: 1200px; height: 902px; overflow: hidden;
    background: var(--backdrop);
    font-family: "Open Sans", Arial, sans-serif;
  }
  .canvas {
    position: relative; width: 1200px; height: 902px;
    display: flex; align-items: center; justify-content: center;
  }
  .business-card {
    position: relative; width: 900px; height: 514px;
    background: radial-gradient(ellipse at 30% 40%, #161616 0%, var(--card-deep) 45%, var(--card-black) 100%);
    box-shadow: 0 18px 40px rgba(0,0,0,.35);
    color: var(--ink-white);
    overflow: hidden;
  }
  .brand {
    position: absolute; left: 300px; top: 92px;
    display: flex; align-items: center; gap: 12px;
  }
  .brand-mark {
    width: 18px; height: 18px;
    background: var(--silver-mid);
  }
  .brand-name {
    font-size: 22px; font-weight: 600; letter-spacing: 3px;
    color: var(--silver-mid); text-transform: uppercase;
  }
  .agents {
    position: absolute; left: 58px; top: 196px;
  }
  .agents-names {
    font-size: 31px; font-weight: 700; color: var(--ink-white);
    letter-spacing: .2px;
  }
  .agents-role {
    font-size: 24px; font-weight: 400; color: var(--ink-grey);
    margin-top: 2px;
  }
  .silver-band {
    position: absolute; left: 0; right: 0; top: 296px; height: 12px;
    background: linear-gradient(180deg, var(--silver-light) 0%, var(--silver-mid) 55%, var(--silver-dark) 100%);
  }
  .contact-list {
    position: absolute; list-style: none;
    display: flex; flex-direction: column; gap: 10px;
  }
  .contact-list li {
    display: flex; align-items: center; gap: 16px;
    font-size: 23px; color: var(--ink-white); letter-spacing: .5px;
  }
  .contact-list svg { width: 20px; height: 20px; flex: none; }
  .contact-office { left: 110px; top: 336px; }
  .contact-site { left: 540px; top: 330px; gap: 18px; }
  .contact-site li { font-size: 19px; }
  .contact-site .address { text-transform: uppercase; letter-spacing: 1px; }
  .contact-site .mobiles { margin-left: 170px; display: flex; flex-direction: column; align-items: flex-start; gap: 8px; }
  .mobile-line { display: flex; align-items: center; gap: 14px; }
</style>
</head>
<body>
<main class="canvas">
  <article class="business-card">
    <div class="brand">
      <span class="brand-mark"></span>
      <span class="brand-name">Walsh &amp; Ortiz Pty Ltd</span>
    </div>

    <header class="agents">
      <h1 class="agents-names">Paul Walsh and Tara Ortiz</h1>
      <p class="agents-role">Sales Agents &amp; Onsite Manager</p>
    </header>

    <div class="silver-band"></div>

    <ul class="contact-list contact-office">
      <li>
        <svg viewBox="0 0 24 24" fill="#fbfbfb"><path d="M6.6 10.8a15 15 0 0 0 6.6 6.6l2.2-2.2c.3-.3.7-.4 1-.2 1.1.4 2.3.6 3.6.6.6 0 1 .4 1 1V20c0 .6-.4 1-1 1A17 17 0 0 1 3 4c0-.6.4-1 1-1h3.5c.6 0 1 .4 1 1 0 1.3.2 2.5.6 3.6.1.3 0 .7-.2 1z"/></svg>
        <span>07 5948 2610</span>
      </li>
      <li>
        <svg viewBox="0 0 24 24" fill="none" stroke="#fbfbfb" stroke-width="2"><rect x="6" y="2" width="12" height="20" rx="2"/><line x1="10" y1="18" x2="14" y2="18"/></svg>
        <span>07 5948 2795</span>
      </li>
      <li>
        <svg viewBox="0 0 24 24" fill="#fbfbfb"><rect x="3" y="8" width="18" height="13" rx="1.5"/><rect x="7" y="3" width="10" height="6" fill="none" stroke="#fbfbfb" stroke-width="1.6"/><rect x="6" y="12" width="12" height="2" fill="#000"/><rect x="6" y="16" width="3" height="2" fill="#000"/><rect x="10.5" y="16" width="3" height="2" fill="#000"/><rect x="15" y="16" width="3" height="2" fill="#000"/></svg>
        <span>M:0451 786 923</span>
      </li>
    </ul>

    <ul class="contact-list contact-site">
      <li class="address">
        <svg viewBox="0 0 24 24" fill="#fbfbfb"><path d="M12 2a7 7 0 0 0-7 7c0 5 7 13 7 13s7-8 7-13a7 7 0 0 0-7-7zm0 9.5A2.5 2.5 0 1 1 12 6.5a2.5 2.5 0 0 1 0 5z"/></svg>
        <span>Kingsmere QLD 4120</span>
      </li>
      <li class="mobiles">
        <span class="mobile-line">
          <svg viewBox="0 0 24 24" fill="none" stroke="#fbfbfb" stroke-width="2"><rect x="6" y="2" width="12" height="20" rx="2"/><line x1="10" y1="18" x2="14" y2="18"/></svg>
          0451786923
        </span>
        <span class="mobile-line">
          <svg viewBox="0 0 24 24" fill="none" stroke="#fbfbfb" stroke-width="2"><rect x="6" y="2" width="12" height="20" rx="2"/><line x1="10" y1="18" x2="14" y2="18"/></svg>
          0438215064
        </span>
      </li>
    </ul>
  </article>
</main>
</body>
</html>
```